Ridgeline Orchards Organic Cherry POS card 7x11

We are wanting to create a one-sided 7 x 11 organic cherry card that is eye catching and informative.This should be clear and easy to read and not cluttered. We use these cards as a display in grocery stores, demo stands, and other events to market Organic Ridgeline Sweet Orchards. We have a few facts that we would like displayed on the card (see attachment).

Target Market(s)

Consumers

Industry/Entity Type

Agriculture

Requirements
Must have
• Natural color palettes
• Easy to read
• Ridgeline Orchards
Nice to have
• Unique, realistic cherry design

```html
<!DOCTYPE html>
<html lang="en">
<head>
<meta charset="utf-8">
<title>Ridgeline Orchards – Organic Cherry Card</title>
<link rel="stylesheet" href="https://fonts.googleapis.com/css2?family=Anton&family=Roboto+Condensed:wght@300;700&display=swap">
<style>
  :root {
    --backdrop: #ece7e2;
    --card: #ffffff;
    --ink: #1b1b1b;
    --cherry: #9a1c3c;
    --gray: #565656;
    --rule: #b98595;
  }
  html, body {
    margin: 0;
    width: 909px;
    height: 1200px;
    overflow: hidden;
    background: var(--backdrop);
  }
  .pos-card {
    position: absolute;
    left: 81px;
    top: 14px;
    width: 746px;
    height: 1172px;
    background: var(--card);
    box-shadow: 0 2px 10px rgba(0,0,0,.12);
    overflow: hidden;
  }
  .cherry-photo {
    position: absolute;
    left: 213px;
    top: 935px;
    width: 320px;
    height: 195px;
    background:
      radial-gradient(ellipse 48% 46% at 50% 55%, #a41c20 0%, #7c1316 55%, rgba(255,255,255,0) 100%);
  }
  .card-art {
    position: absolute;
    inset: 0;
    width: 746px;
    height: 1172px;
  }
  .brand-name { font-family: "Anton", sans-serif; fill: var(--ink); }
  .brand-dot { fill: var(--cherry); }
  .headline { font-family: "Anton", sans-serif; fill: var(--ink); }
  .headline--accent { fill: var(--cherry); }
  .subline {
    font-family: "Roboto Condensed", sans-serif;
    font-weight: 300;
    font-size: 23px;
    letter-spacing: .5px;
    fill: var(--gray);
  }
  .callout-rule { stroke: var(--rule); stroke-width: 1.2; fill: none; }
  .callout-dot { fill: var(--cherry); }
  .callout-label {
    font-family: "Roboto Condensed", sans-serif;
    font-weight: 700;
    font-size: 31px;
    fill: var(--gray);
  }
</style>
</head>
<body>
  <main class="pos-card">
    <div class="cherry-photo" role="img" aria-label="Photo of two glossy red organic cherries with crossed green stems"></div>

    <svg class="card-art" viewBox="0 0 746 1172" xmlns="http://www.w3.org/2000/svg">
      <g class="brand">
        <circle class="brand-dot" cx="218" cy="90" r="22"/>
        <text class="brand-name" x="254" y="108" font-size="48">Ridgeline Orchards</text>
      </g>

      <text class="headline" x="96" y="303" font-size="168" textLength="552" lengthAdjust="spacingAndGlyphs">ORGANIC</text>
      <text class="headline headline--accent" x="96" y="378" font-size="68" textLength="554" lengthAdjust="spacingAndGlyphs">RIDGELINE ORCHARDS</text>
      <text class="headline" x="118" y="450" font-size="68" textLength="511" lengthAdjust="spacingAndGlyphs">MAKE UP 1/3 OF THE</text>
      <text class="headline" x="96" y="521" font-size="68" textLength="555" lengthAdjust="spacingAndGlyphs">NATION’S PRODUCTION</text>

      <text class="subline" x="373" y="567" text-anchor="middle">WASHINGTON STATE IS THE NATION’S</text>
      <text class="subline" x="373" y="603" text-anchor="middle">LARGEST PRODUCER OF ORGANIC CHERRIES</text>

      <g class="callouts callouts--left">
        <polyline class="callout-rule" points="81,664 270,664 305,698"/>
        <circle class="callout-dot" cx="305" cy="698" r="3"/>
        <text class="callout-label" x="267" y="708" text-anchor="end">Fat Free</text>

        <polyline class="callout-rule" points="81,750 270,750 305,785"/>
        <circle class="callout-dot" cx="305" cy="785" r="3"/>
        <text class="callout-label" x="267" y="794" text-anchor="end">Vitamin C</text>

        <polyline class="callout-rule" points="81,834 270,834 305,870"/>
        <circle class="callout-dot" cx="305" cy="870" r="3"/>
        <text class="callout-label" x="267" y="882" text-anchor="end">Potassium</text>
      </g>

      <g class="callouts callouts--right">
        <polyline class="callout-rule" points="659,751 463,751 423,786"/>
        <circle class="callout-dot" cx="423" cy="786" r="3"/>
        <text class="callout-label" x="464" y="796">Natural Anti-</text>
        <text class="callout-label" x="464" y="831">Inflammatory</text>

        <polyline class="callout-rule" points="659,870 463,870 423,904"/>
        <circle class="callout-dot" cx="423" cy="904" r="3"/>
        <text class="callout-label" x="464" y="913">Melatonin</text>
      </g>
    </svg>
  </main>
</body>
</html>
```